Business Card Design Project

Use our current logo. Clean design.

Industry/Entity Type

Business

Requirements
Must have
• Marisela DUBRANCQ
M. Law
Managing Partner

Alpenvorsa AG
Kornhalmweg 214
CH-3097 Liebefeld

M. +41 79 412 56 27
T. +41 31 928 44 10
F. +41 31 928 44 19

m.dubrancq@alpenvorsa-example.com
www.alpenvorsa-example.com

```html
<!DOCTYPE html>
<html lang="en">
<head>
<meta charset="UTF-8">
<title>Alpenvorsa AG – Business Card</title>
<link rel="stylesheet" href="https://fonts.googleapis.com/css2?family=Tinos:wght@400&display=swap">
<style>
  :root {
    --backdrop: #4b2a1c;
    --card-white: #f1f1f1;
    --card-white-edge: #e4e4e4;
    --charcoal: #3a3b3d;
    --charcoal-dark: #2f3032;
    --crimson: #9e1f22;
    --crimson-light: #a8262a;
    --ink: #1f1f1f;
    --paper-text: #f4f4f4;
  }
  * { box-sizing: border-box; margin: 0; padding: 0; }
  html, body {
    width: 936px;
    height: 1200px;
    overflow: hidden;
    background: var(--backdrop);
    font-family: "Tinos", "Times New Roman", serif;
  }
  .canvas {
    position: relative;
    width: 936px;
    height: 1200px;
  }
  .card {
    position: absolute;
    left: 162px;
    width: 600px;
    background: linear-gradient(180deg, var(--card-white) 0%, var(--card-white-edge) 100%);
    box-shadow: 0 4px 10px rgba(0,0,0,0.45);
    overflow: hidden;
  }
  .card-front { top: 196px; height: 343px; }
  .card-back  { top: 615px; height: 346px; }

  .top-band {
    position: absolute;
    left: 0; top: 0;
    width: 100%; height: 11px;
    background: var(--charcoal);
  }

  .wordmark {
    position: absolute;
    left: 0; right: 0;
    text-align: center;
    color: var(--ink);
    font-size: 26px;
    letter-spacing: 1px;
    line-height: 1;
  }
  .card-front .wordmark { top: 158px; }

  .bottom-strip {
    position: absolute;
    left: 0; bottom: 0;
    width: 100%; height: 9px;
  }
  .strip-piece { position: absolute; top: 0; height: 100%; }
  .strip-dark { background: var(--charcoal); }
  .strip-red  { background: var(--crimson); }

  .name-tab {
    position: absolute;
    left: 0; top: 71px;
    width: 310px; height: 107px;
    background: var(--charcoal);
    border-radius: 0 6px 6px 0;
    display: flex;
    align-items: center;
    padding-left: 36px;
  }
  .person-name {
    color: var(--paper-text);
    font-size: 22px;
  }
  .card-back .wordmark {
    left: 318px; right: 126px;
    top: 113px;
    font-size: 20px;
  }
  .title-tab {
    position: absolute;
    left: 481px; top: 71px;
    width: 119px; height: 107px;
    background: var(--charcoal);
    border-radius: 6px 0 0 6px;
    display: flex;
    align-items: center;
    justify-content: flex-start;
    padding-left: 4px;
  }
  .title-lines {
    writing-mode: vertical-rl;
    color: var(--paper-text);
    font-size: 11px;
    line-height: 1.25;
    text-align: center;
  }
  .divider-band {
    position: absolute;
    left: 0; top: 240px;
    width: 100%; height: 8px;
    background: var(--charcoal);
  }
  .info-panel {
    position: absolute;
    top: 254px; height: 92px;
    display: flex;
    flex-direction: column;
    justify-content: center;
    align-items: center;
    color: var(--paper-text);
    font-size: 10px;
    line-height: 1.3;
    text-align: center;
  }
  .panel-phone   { left: 0;     width: 188px; background: var(--charcoal); }
  .panel-web     { left: 194px; width: 211px; background: linear-gradient(180deg, var(--crimson-light), var(--crimson)); }
  .panel-address { left: 410px; width: 190px; background: var(--charcoal); }
  .phone-list { text-align: left; }
</style>
</head>
<body>
<main class="canvas">

  <section class="card card-front" aria-label="Card front">
    <div class="top-band"></div>
    <p class="wordmark">ALPENVORSA</p>
    <div class="bottom-strip">
      <span class="strip-piece strip-dark" style="left:0;width:173px"></span>
      <span class="strip-piece strip-red" style="left:179px;width:211px"></span>
      <span class="strip-piece strip-dark" style="left:396px;width:204px"></span>
    </div>
  </section>

  <section class="card card-back" aria-label="Card back">
    <div class="top-band"></div>
    <div class="name-tab"><p class="person-name">Marisela DUBRANCQ</p></div>
    <p class="wordmark">ALPENVORSA</p>
    <div class="title-tab">
      <p class="title-lines">M. Law<br>Managing Partner</p>
    </div>
    <div class="divider-band"></div>

    <div class="info-panel panel-phone">
      <p class="phone-list">M. +41 79 412 56 27<br>T. +41 31 928 44 10<br>F. +41 31 928 44 19</p>
    </div>
    <div class="info-panel panel-web">
      <p>m.dubrancq@alpenvorsa-example.com<br>www.alpenvorsa-example.com</p>
    </div>
    <div class="info-panel panel-address">
      <p>Alpenvorsa AG<br>Kornhalmweg 214<br>CH-3097 Liebefeld</p>
    </div>
  </section>

</main>
</body>
</html>
```